Quillmarsh Trades Landing Page

I need a landing page for a campaign advertising quillmarsh trades trading. The campaign and overall look and feel should be inspired by this brand: https://quillmarshtrades.com/

The screenshots you want to add from the trading area you can simple google. We will replace any screenshots with actual screenshots from our binary trading software.

You can also copy the text since we will replace the text as well.

The name to advertise is "Tandel Pilot - Harvest Methods" and will be featured on www.tandelpilot.ws

What is important is the overall look!
- Tandel Pilot
- Clean Design
- Nice colors
- Makes you want to signup and trade!

Target Market(s)

People who wants to earn some extra money by investing and trading options online.

Industry/Entity Type

Advertising

Logo Text

TAndelPilot - Harvest Method

Number of Pages Required

1 page

Colors

Designer to choose colors to be used in the design.

Requirements
Must have
• New Logo or remake of current logo
• Design for web resolution
• Design for mobile resolution
• Signup form as attached but designed more flashy!
• The chat popup may not block crucial elements of the design
Nice to have
• Screenshots that makes people interested to signup
• Catchy phrases that will get people interested in the product
• You are allowed to copy or partly copy the current logo
• Design a contact page
Should not have
• US flags

```html
<!DOCTYPE html>
<html lang="en">
<head>
<meta charset="utf-8">
<title>Tandel Pilot - Harvest Methods</title>
<link href="https://fonts.googleapis.com/css2?family=Montserrat:wght@400;600;700&family=Open+Sans:wght@400;600&family=Michroma&display=swap" rel="stylesheet">
<style>
:root{
  --navy:#0d3560;
  --navy-deep:#0a2c52;
  --orange:#f26522;
  --ink:#222;
  --muted:#777;
  --line:#e2e2e2;
  --row:#f7f7f7;
  --dark:#1c1f22;
}
*{margin:0;padding:0;box-sizing:border-box}
html,body{width:1200px;height:2679px;overflow:hidden;background:#fff}
body{position:relative;font-family:'Open Sans',sans-serif;color:var(--ink)}
.abs{position:absolute}
.heading{font-family:'Michroma','Montserrat',sans-serif;text-align:center;left:0;width:1200px;color:#111}
.lead{font-size:12px;line-height:20px;color:#666;text-align:center;left:250px;width:700px}

/* header */
.site-header{top:0;left:0;width:1200px;height:75px;background:#fff}
.brand{left:132px;top:24px;font-family:'Montserrat',sans-serif;font-weight:700;font-size:24px;color:var(--navy);letter-spacing:.3px}
.nav a{position:absolute;top:31px;font-family:'Montserrat',sans-serif;font-size:11px;font-weight:600;color:#222;text-decoration:none;transform:translateX(-50%)}
.nav .active{color:var(--navy)}
.nav .pointer{position:absolute;left:539px;top:66px;border:6px solid transparent;border-bottom-color:var(--navy)}
.btn-login{left:997px;top:21px;width:71px;height:34px;border-radius:17px;background:var(--orange);color:#fff;font-family:'Montserrat',sans-serif;font-weight:700;font-size:10.5px;display:flex;align-items:center;justify-content:center}
.header-band{top:75px;left:0;width:1200px;height:6px;background:var(--navy)}

/* hero */
.hero-photo{top:81px;left:0;width:1200px;height:640px;background:
  radial-gradient(ellipse 140px 110px at 600px 150px,rgba(190,150,130,.55),transparent 70%),
  radial-gradient(ellipse 90px 70px at 430px 300px,rgba(255,255,255,.35),transparent 70%),
  radial-gradient(ellipse 120px 90px at 500px 420px,rgba(230,60,40,.35),transparent 70%),
  radial-gradient(ellipse 110px 80px at 560px 400px,rgba(60,200,120,.25),transparent 70%),
  radial-gradient(ellipse 320px 170px at 470px 380px,rgba(70,130,190,.65),transparent 72%),
  linear-gradient(160deg,#0a0d12 0%,#101a26 40%,#1d2c3c 60%,#07090c 85%)}
.hero-title{left:150px;top:143px;font-family:'Michroma',sans-serif;font-size:24px;color:#fff;font-weight:400}
.hero-sub{left:150px;top:206px;width:450px;font-size:13px;line-height:25px;color:#fff;font-weight:600}
.badge{top:506px;width:150px;text-align:center;color:#fff;font-family:'Montserrat',sans-serif;font-size:10px;font-weight:600;line-height:19px}
.badge .mark{width:52px;height:52px;border-radius:50%;border:3px solid #fff;margin:0 auto 14px;display:flex;align-items:center;justify-content:center}
.badge .mark::after{content:"";width:26px;height:26px;border-radius:50%;background:#fff}
.badge-sep{top:506px;width:1px;height:104px;background:rgba(255,255,255,.25)}
.pay{top:528px;width:40px;height:40px;border-radius:5px;border:2px solid #fff;background:rgba(255,255,255,.12)}
.dot{top:602px;width:15px;height:15px;border-radius:50%;border:2px solid #fff}
.dot.on{background:var(--orange);border-color:var(--orange)}

.signup{left:771px;top:129px;width:297px;height:378px;border:2px solid #3b4654;background:rgba(20,24,30,.6)}
.signup-head{height:50px;background:var(--navy);color:#fff;font-family:'Montserrat',sans-serif;font-weight:600;font-size:16px;text-align:center;line-height:50px}
.field{position:absolute;left:23px;width:247px;height:36px;border:1.5px solid #e9e9e9;border-radius:3px;color:#fff;font-size:10.5px;line-height:33px;padding-left:12px}
.btn-contact{position:absolute;left:79px;top:315px;width:136px;height:39px;border-radius:20px;background:var(--orange);color:#fff;font-family:'Montserrat',sans-serif;font-weight:700;font-size:10.5px;text-align:center;line-height:39px}

/* features */
.feature-visual{left:132px;top:791px;width:322px;height:345px;border-radius:6px;background:
  radial-gradient(ellipse 60px 50px at 150px 190px,rgba(120,200,255,.8),transparent 70%),
  linear-gradient(180deg,#2f67b0 0%,#18407e 55%,#0e1a2c 62%,#b8bcc2 70%,#eceef0 100%)}
.feature-icon{left:531px;width:64px;height:64px;border-radius:50%;border:2px solid var(--navy);display:flex;align-items:center;justify-content:center}
.feature-title{left:614px;font-family:'Montserrat',sans-serif;font-weight:600;font-size:11.5px;color:#111}
.feature-text{left:614px;width:410px;font-size:10px;line-height:19px;color:#777}
.scroll-track{left:1061px;top:813px;width:5px;height:244px;background:#eee}
.scroll-thumb{left:1061px;top:943px;width:5px;height:40px;background:#555}

/* table */
.tabs{left:132px;top:1192px;width:936px;height:53px;display:flex}
.tab{flex:1;background:var(--dark);color:#fff;font-family:'Montserrat',sans-serif;font-size:12.5px;display:flex;align-items:center;justify-content:center;border-left:1px solid #333}
.tab.active{background:var(--navy);border-left:none}
.trade-table{left:132px;top:1245px;width:936px;border:1px solid var(--line);border-top:none}
.trade-table .row{display:grid;grid-template-columns:136px 180px 154px 150px 153px 163px;align-items:center;height:59px;border-top:1px solid var(--line);font-size:10.5px;color:#444;text-align:center;background:var(--row)}
.trade-table .head{height:50px;background:#fff;font-family:'Montserrat',sans-serif;font-weight:600;font-size:10.5px;color:#222;border-top:none}
.broker{font-family:'Open Sans',sans-serif;font-size:16px;color:#333;letter-spacing:-.3px;padding-left:18px}
.toggle{display:inline-flex;width:66px;height:28px;border-radius:14px;background:#fff;box-shadow:0 1px 4px rgba(0,0,0,.25);overflow:hidden}
.toggle span{width:38px;background:var(--orange);color:#fff;font-size:10px;line-height:28px}
.btn-deposit{display:inline-block;width:72px;height:27px;border-radius:14px;background:var(--navy);color:#fff;font-size:10px;font-weight:600;line-height:27px}

/* advantages */
.adv-divider-v{left:380px;top:1652px;width:1px;height:392px;background:var(--line)}
.adv-divider-h{left:132px;top:1845px;width:497px;height:1px;background:var(--line)}
.adv{width:260px;text-align:center}
.adv svg{display:block;margin:0 auto}
.adv-title{font-family:'Montserrat',sans-serif;font-weight:700;font-size:11.5px;color:#111;margin-top:14px}
.adv-text{font-size:10px;line-height:20px;color:#777;margin-top:6px}
.adv-visual{left:679px;top:1729px;width:389px;height:316px;border-radius:12px;border:10px solid #161616;box-shadow:0 6px 14px rgba(0,0,0,.25);background:
  radial-gradient(ellipse 50px 45px at 110px 110px,rgba(40,200,70,.7),transparent 70%),
  radial-gradient(ellipse 50px 45px at 210px 120px,rgba(230,40,40,.7),transparent 70%),
  linear-gradient(180deg,#0f0f0f 0%,#1e0a0a 50%,#7a1414 85%,#a51b1b 100%)}
.btn-start{left:132px;top:2073px;width:157px;height:45px;border-radius:23px;background:var(--navy);color:#fff;font-family:'Montserrat',sans-serif;font-weight:700;font-size:10px;text-align:center;line-height:45px}

/* steps */
.steps{left:0;top:2204px;width:1200px;height:373px;background:var(--navy)}
.steps .heading{color:#fff}
.steps .lead{color:#fff}
.step-line{top:2422px;left:309px;width:579px;height:6px;background:#fff}
.step-circle{top:2366px;width:118px;height:118px;border-radius:50%;background:var(--navy);border:4px solid #fff;display:flex;align-items:center;justify-content:center}
.step-num{width:38px;height:38px;border-radius:50%;background:var(--orange);border:3px solid #fff;color:#fff;font-family:'Montserrat',sans-serif;font-weight:700;font-size:14px;display:flex;align-items:center;justify-content:center}
.step-label{top:2498px;width:200px;text-align:center;color:#fff;font-family:'Montserrat',sans-serif;font-weight:700;font-size:11.5px}

/* footer */
.footer-links{left:132px;top:2605px;font-size:9.5px;color:#444;word-spacing:2px}
.copyright{left:132px;top:2637px;font-size:9px;color:#444}
.connect{left:866px;top:2622px;font-size:8.5px;color:#444}
.social{top:2615px;width:24px;height:24px;border-radius:50%;border:1.5px solid var(--navy)}
</style>
</head>
<body>

<header class="abs site-header">
  <div class="abs brand">TANDEL PILOT</div>
  <nav class="nav">
    <a class="active" style="left:546px">HOME</a>
    <a style="left:627px">ABOUT US</a>
    <a style="left:720px">SERVICES</a>
    <a style="left:795px">FAQ</a>
    <a style="left:862px">GUIDES</a>
    <a style="left:945px">CONTACT</a>
    <span class="pointer"></span>
  </nav>
  <div class="abs btn-login">LOGIN</div>
</header>
<div class="abs header-band"></div>

<section>
  <div class="abs hero-photo" role="img" aria-label="Hand touching a smartphone showing glowing currency symbols and trading charts"></div>
  <h1 class="abs hero-title">Tandel Pilot - Harvest Methods</h1>
  <p class="abs hero-sub">Lorem ipsum dolor sit amet, consectetur adipiscing elit, sed do eiusmod tempor incididunt ut labore et dolore..</p>

  <div class="abs badge" style="left:112px"><div class="mark"></div>BEST TANDEL PILOT<br>2017</div>
  <div class="abs badge-sep" style="left:259px"></div>
  <div class="abs badge" style="left:265px"><div class="mark"></div>TOP TRADING PLATFORM</div>
  <div class="abs badge-sep" style="left:425px"></div>
  <div class="abs badge" style="left:427px"><div class="mark"></div>FRIENDLY CUSTOMER<br>SUPPORT</div>

  <form class="abs signup">
    <div class="signup-head">ACCOUNT INFORMATION</div>
    <div class="field" style="top:64px">First Name</div>
    <div class="field" style="top:112px">Last Name</div>
    <div class="field" style="top:160px">Password</div>
    <div class="field" style="top:208px">Valid E-mail Address</div>
    <div class="field" style="top:257px;width:118px">+345</div>
    <div class="field" style="top:257px;left:152px;width:118px">Phone</div>
    <div class="btn-contact">CONTACT US</div>
  </form>

  <div class="abs pay" style="left:808px"></div>
  <div class="abs pay" style="left:862px"></div>
  <div class="abs pay" style="left:918px;width:52px"></div>
  <div class="abs pay" style="left:988px;border-radius:50%"></div>

  <div class="abs dot on" style="left:989px"></div>
  <div class="abs dot" style="left:1021px"></div>
  <div class="abs dot" style="left:1054px"></div>

  <svg class="abs" style="left:0;top:620px" width="1200" height="110" viewBox="0 0 1200 110">
    <path d="M0 110 L0 86 Q600 -10 1200 86 L1200 110 Z" fill="#fff"/>
    <path d="M40 104 Q600 -30 1160 104" fill="none" stroke="#f26522" stroke-width="4"/>
  </svg>
</section>

<section>
  <h2 class="abs heading" style="top:708px;font-size:23px">FEATURES TO TANDEL PILOT</h2>
  <p class="abs lead" style="top:741px">Lorem ipsum dolor sit amet, consectetur adipiscing elit, sed do eiusmod tempor incididunt ut labore et dolore magna aliqua. Ut enim ad minim veniam, quis nostrud exercitation ullamco laboris nisi</p>

  <div class="abs feature-visual" role="img" aria-label="Desktop monitor displaying a globe and trading charts"></div>

  <div class="abs feature-icon" style="top:834px">
    <svg width="26" height="26" viewBox="0 0 24 24" fill="none" stroke="#0d3560" stroke-width="2"><path d="M7 11v9H3v-9zM7 11l4-8a2 2 0 0 1 3 2l-1 5h6a2 2 0 0 1 2 2l-2 7a2 2 0 0 1-2 1H7"/></svg>
  </div>
  <div class="abs feature-title" style="top:837px">Safe &amp; Secure - Automatic stop loss</div>
  <div class="abs feature-text" style="top:858px">Lorem Ipsum is simply dummy text of the printing and typesetting industry. Lorem Ipsum has been the industry's occaecat cupidatat...</div>

  <div class="abs feature-icon" style="top:930px">
    <svg width="26" height="26" viewBox="0 0 24 24" fill="none" stroke="#0d3560" stroke-width="2"><path d="M12 2v20M17 6H10a3 3 0 0 0 0 6h4a3 3 0 0 1 0 6H6"/></svg>
  </div>
  <div class="abs feature-title" style="top:933px">No Downloads - No Charges</div>
  <div class="abs feature-text" style="top:954px">Lorem Ipsum is simply dummy text of the printing and typesetting industry. Lorem Ipsum has been the industry's occaecat cupidatat...</div>

  <div class="abs feature-icon" style="top:1027px">
    <svg width="26" height="26" viewBox="0 0 24 24" fill="#0d3560"><path d="M6 3h12v5a6 6 0 0 1-12 0zM3 4h3v3a3 3 0 0 1-3-3zM21 4h-3v3a3 3 0 0 0 3-3zM11 14h2v4h3v3H8v-3h3z"/></svg>
  </div>
  <div class="abs feature-title" style="top:1030px">Trusted Tandel Pilot</div>
  <div class="abs feature-text" style="top:1051px">Lorem Ipsum is simply dummy text of the printing and typesetting industry. Lorem Ipsum has been the industry's occaecat cupidatat...</div>

  <div class="abs scroll-track"></div>
  <div class="abs scroll-thumb"></div>
</section>

<section>
  <div class="abs tabs">
    <div class="tab active">Robot Settings</div>
    <div class="tab">History</div>
    <div class="tab">Profile</div>
  </div>
  <div class="abs trade-table">
    <div class="row head"><div>Brokers</div><div>Balance</div><div>Open Trades</div><div>Profit</div><div>Active Trading</div><div>Deposit</div></div>
    <div class="row"><div class="broker">Company</div><div>£8,459.50</div><div>£0</div><div>£2,567.00</div><div><span class="toggle"><span>ON</span></span></div><div><span class="btn-deposit">DEPOST</span></div></div>
    <div class="row"><div class="broker">Company</div><div>£8,459.50</div><div>£0</div><div>£2,567.00</div><div><span class="toggle"><span>ON</span></span></div><div><span class="btn-deposit">DEPOST</span></div></div>
    <div class="row"><div class="broker">Company</div><div>£8,459.50</div><div>£0</div><div>£2,567.00</div><div><span class="toggle"><span>ON</span></span></div><div><span class="btn-deposit">DEPOST</span></div></div>
  </div>
</section>

<section>
  <h2 class="abs heading" style="top:1533px;font-size:23px">TANDEL PILOT TRADING ADVANTAGES</h2>
  <p class="abs lead" style="top:1569px">Lorem ipsum dolor sit amet, consectetur adipiscing elit, sed do eiusmod tempor incididunt ut labore et dolore magna aliqua. Ut enim ad minim veniam, quis nostrud exercitation ullamco laboris nisi</p>

  <div class="abs adv-divider-v"></div>
  <div class="abs adv-divider-h"></div>

  <div class="abs adv" style="left:116px;top:1672px">
    <svg width="62" height="56" viewBox="0 0 62 56"><path d="M31 2 L60 54 H2 Z" fill="#f26522"/><rect x="28" y="18" width="6" height="20" fill="#fff"/><rect x="28" y="42" width="6" height="6" fill="#fff"/></svg>
    <div class="adv-title">No Emotions</div>
    <div class="adv-text">Lorem ipsum dolor sit amet, consectetur adipi-<br>scing elit, sed do eiusmod tempor incididunt ut<br>labore et dolore magna...</div>
  </div>
  <div class="abs adv" style="left:380px;top:1672px">
    <svg width="52" height="56" viewBox="0 0 52 56"><rect x="24" y="0" width="4" height="8" fill="#f26522"/><rect x="8" y="8" width="36" height="26" rx="8" fill="#f26522"/><circle cx="19" cy="21" r="4" fill="#fff"/><circle cx="33" cy="21" r="4" fill="#fff"/><rect x="12" y="37" width="28" height="16" rx="3" fill="#f26522"/><rect x="2" y="16" width="5" height="12" fill="#f26522"/><rect x="45" y="16" width="5" height="12" fill="#f26522"/></svg>
    <div class="adv-title">Sequence</div>
    <div class="adv-text">Lorem ipsum dolor sit amet, consectetur adipi-<br>scing elit, sed do eiusmod tempor incididunt ut<br>labore et dolore magna...</div>
  </div>
  <div class="abs adv" style="left:116px;top:1870px">
    <svg width="62" height="56" viewBox="0 0 62 56"><path d="M16 42 A12 12 0 0 1 14 18 A17 17 0 0 1 46 14 A13 13 0 0 1 48 42 Z" fill="#f26522"/><path d="M31 20 V40 M23 32 L31 40 L39 32" stroke="#fff" stroke-width="4" fill="none"/><rect x="22" y="47" width="18" height="4" fill="#f26522"/></svg>
    <div class="adv-title">No Download</div>
    <div class="adv-text">Lorem ipsum dolor sit amet, consectetur adipi-<br>scing elit, sed do eiusmod tempor incididunt ut<br>labore et dolore magna...</div>
  </div>
  <div class="abs adv" style="left:380px;top:1870px">
    <svg width="56" height="56" viewBox="0 0 56 56"><rect x="4" y="10" width="40" height="42" fill="none" stroke="#f26522" stroke-width="5"/><path d="M22 38 L48 8 L54 14 L28 42 L20 44 Z" fill="#f26522"/></svg>
    <div class="adv-title">Ability to Open VIP Account</div>
    <div class="adv-text">Lorem ipsum dolor sit amet, consectetur adipi-<br>scing elit, sed do eiusmod tempor incididunt ut<br>labore et dolore magna...</div>
  </div>

  <div class="abs adv-visual" role="img" aria-label="Tablet showing a trading chart with call and put buttons"></div>
  <div class="abs btn-start">GET STARTED TODAY</div>
</section>

<section class="abs steps">
  <h2 class="abs heading" style="top:62px;font-size:23px">GET STARTED IN 3 EASY STEPS</h2>
  <p class="abs lead" style="top:97px">Lorem ipsum dolor sit amet, consectetur adipiscing elit, sed do eiusmod tempor incididunt ut labore et dolore magna aliqua. Ut enim ad minim veniam, quis nostrud exercitation ullamco laboris nisi</p>
</section>
<div class="abs step-line"></div>

<div class="abs step-circle" style="left:250px">
  <svg width="46" height="50" viewBox="0 0 46 50" fill="#fff"><circle cx="23" cy="13" r="11"/><path d="M3 50 A20 20 0 0 1 43 50 Z"/></svg>
</div>
<div class="abs step-num" style="left:334px;top:2362px">1</div>
<div class="abs step-label" style="left:209px">Open a free account</div>

<div class="abs step-circle" style="left:539px">
  <svg width="56" height="44" viewBox="0 0 56 44" fill="none" stroke="#fff" stroke-width="3.5"><rect x="2" y="12" width="42" height="28" rx="3"/><path d="M10 12 L14 3 L54 12 L48 34"/><path d="M2 20 H44"/></svg>
</div>
<div class="abs step-num" style="left:623px;top:2362px">2</div>
<div class="abs step-label" style="left:498px">Deposit (no fees!)</div>

<div class="abs step-circle" style="left:829px">
  <svg width="46" height="52" viewBox="0 0 46 52"><path d="M15 2 H31 L26 12 H20 Z" fill="#fff"/><path d="M19 14 H27 C42 22 46 36 42 44 C39 50 7 50 4 44 C0 36 4 22 19 14Z" fill="#fff"/><text x="23" y="42" text-anchor="middle" font-family="Montserrat,sans-serif" font-weight="700" font-size="20" fill="#0d3560">$</text></svg>
</div>
<div class="abs step-num" style="left:913px;top:2362px">3</div>
<div class="abs step-label" style="left:788px">Begin robot trading!</div>

<footer>
  <div class="abs footer-links">HOME &nbsp;| &nbsp;ABOUT US &nbsp;| &nbsp;SERVICES &nbsp;| &nbsp;FAQ &nbsp;| &nbsp;GUIDES &nbsp;| &nbsp;CONTACT</div>
  <div class="abs copyright">COPYRIGHTS © TANDELPILOT . 2017 | ALL RIGHTS RESERVED.</div>
  <div class="abs connect">CONNECT WITH US :</div>
  <div class="abs social" style="left:960px"></div>
  <div class="abs social" style="left:988px"></div>
  <div class="abs social" style="left:1016px"></div>
  <div class="abs social" style="left:1044px"></div>
</footer>

</body>
</html>
```